BUsiness Card

We need a unique business card design for a new aesthetic practice, Meadowlark Aesthetics & Wellness, P.A. The reverse of the card should be an appointment card.

```html
<!DOCTYPE html>
<html lang="en">
<head>
<meta charset="utf-8">
<title>Meadowlark Aesthetics &amp; Wellness – Business &amp; Appointment Card</title>
<link rel="stylesheet" href="https://fonts.googleapis.com/css2?family=Raleway:wght@500;600;700;800&family=Marcellus&display=swap">
<style>
  :root {
    --navy: #0d4560;
    --teal: #17a99a;
    --paper: #ffffff;
    --mist: #e7e8ea;
    --stage: #eef0f2;
    --ink: #0d4560;
  }
  * { box-sizing: border-box; margin: 0; padding: 0; }
  html, body { width: 1200px; height: 863px; overflow: hidden; }
  body {
    background: var(--stage);
    font-family: "Raleway", sans-serif;
    color: var(--ink);
    position: relative;
  }
  .card {
    position: absolute;
    top: 169px;
    width: 300px;
    height: 525px;
    background: var(--paper);
    box-shadow: 0 6px 24px rgba(13, 69, 96, 0.15);
    overflow: hidden;
  }
  .card--appointment { left: 270px; }
  .card--business { left: 630px; }

  .wordmark {
    position: absolute;
    left: 0; right: 0;
    text-align: center;
    color: var(--navy);
    font-family: "Raleway", sans-serif;
    font-weight: 700;
  }
  .wordmark__dot {
    display: block;
    width: 58px; height: 58px;
    margin: 0 auto 12px;
    border-radius: 50%;
    background: var(--navy);
  }
  .wordmark__name { display: block; font-size: 30px; letter-spacing: 1px; line-height: 1; text-transform: uppercase; }
  .wordmark__tag { display: block; font-size: 10.5px; letter-spacing: 2.4px; margin-top: 6px; text-transform: uppercase; }
  .card--appointment .wordmark { top: 42px; }
  .card--business .wordmark { top: 62px; }

  .band {
    position: absolute;
    left: 0; right: 0;
    text-align: center;
  }
  .band::after {
    content: "";
    position: absolute;
    left: 50%;
    bottom: -10px;
    transform: translateX(-50%);
    border-left: 10px solid transparent;
    border-right: 10px solid transparent;
    border-top: 10px solid currentColor;
  }
  .band--appointment {
    top: 178px; height: 62px;
    background: var(--teal);
    color: var(--teal);
  }
  .band__title {
    display: block;
    font-family: "Marcellus", serif;
    font-size: 25px;
    letter-spacing: 1.5px;
    color: var(--paper);
    line-height: 62px;
    text-transform: uppercase;
  }
  .band--person {
    top: 222px; height: 66px;
    background: var(--navy);
    color: var(--navy);
    padding-top: 13px;
  }
  .band__name { display: block; font-weight: 800; font-size: 18px; letter-spacing: 1px; color: var(--paper); }
  .band__role { display: block; font-weight: 600; font-size: 12px; letter-spacing: 1.5px; color: var(--teal); margin-top: 3px; text-transform: uppercase; }

  .texture {
    position: absolute;
    left: 0; right: 0;
    top: 240px; height: 255px;
    background: linear-gradient(180deg, #f3f4f5, var(--mist));
  }
  .schedule {
    position: absolute;
    left: 40px; right: 30px;
    top: 300px;
    list-style: none;
  }
  .schedule__row {
    display: flex;
    align-items: flex-end;
    gap: 12px;
    margin-bottom: 20px;
  }
  .schedule__label {
    font-weight: 700;
    font-size: 11px;
    letter-spacing: 2.5px;
    color: var(--teal);
    text-transform: uppercase;
  }
  .schedule__line { flex: 1; border-bottom: 1.5px solid var(--navy); height: 1px; }

  .footer-band { position: absolute; left: 0; right: 0; bottom: 0; height: 30px; }
  .footer-band--navy { background: var(--navy); }
  .footer-band--teal { background: var(--teal); }

  .contact {
    position: absolute;
    left: 0; right: 0;
    top: 328px;
    text-align: center;
    font-weight: 500;
    font-size: 12.5px;
    line-height: 1.4;
    color: var(--navy);
    font-style: normal;
  }
  .contact__group + .contact__group { margin-top: 20px; }
  .contact__group span { display: block; }
</style>
</head>
<body>
  <section class="card card--appointment" aria-label="Appointment card">
    <div class="wordmark">
      <span class="wordmark__dot"></span>
      <span class="wordmark__name">Meadowlark</span>
      <span class="wordmark__tag">Aesthetics &amp; Wellness</span>
    </div>
    <div class="texture" role="img" aria-label="Soft grey wood-grain line texture behind the appointment fields"></div>
    <div class="band band--appointment"><span class="band__title">Appointment</span></div>
    <ul class="schedule">
      <li class="schedule__row"><span class="schedule__label">Date</span><span class="schedule__line"></span></li>
      <li class="schedule__row"><span class="schedule__label">Time</span><span class="schedule__line"></span></li>
    </ul>
    <div class="footer-band footer-band--navy"></div>
  </section>

  <section class="card card--business" aria-label="Business card">
    <div class="wordmark">
      <span class="wordmark__dot"></span>
      <span class="wordmark__name">Meadowlark</span>
      <span class="wordmark__tag">Aesthetics &amp; Wellness</span>
    </div>
    <div class="band band--person">
      <span class="band__name">AVERY LANE</span>
      <span class="band__role">Owner</span>
    </div>
    <address class="contact">
      <div class="contact__group">
        <span>Call +1 410-555-0182</span>
        <span>www.meadowlark-aesthetics.com</span>
      </div>
      <div class="contact__group">
        <span>2270 Harbor View Rd, Suite 104</span>
        <span>Easton, Maryland</span>
      </div>
    </address>
    <div class="footer-band footer-band--teal"></div>
  </section>
</body>
</html>
```